Honey Labels for Manuka, Rewarewa, Multifloral and Manuka Blend honey

We require 4 label designs for our 4 types of honey i.e. Manuka, Rewarewa, Multifloral and Manuka Blend. Each design should be adapted for 250g, 500g, and 1kg PET jars. The design should look friendly and professional.

Tare: amber Square mason PET jars (see images attached)
Jar dimensions: see PDF attached

Target Market(s)

Worldwide. People caring for their health.

Industry/Entity Type

Health Product

Font styles to use
Serif
Decorative

Colors
6a429a
f37122
0692cd
9bcb3c

Requirements
Must have
• Each label should contain the following information
• • name of the honey e.g. Manuka Honey
• • VelnorTM logo (provided)
• • an image of a bird (provided),
• • nutrition table
• • a bar code
• • a place for a batch number and the best before date to be printed
• • volume: e.g. 250g, 500g, 1kg
• • Text: “Product of New Zealand”
• • Text: “Produced & packed by: Dostrel’s Combs Ltd. 87B Kelvanie Road, Tauranga 3148, New Zealand sales@velnorhoney.co.nz www.velnorhoney.co.nz
• • Ingredients: 100% Pure Raw New Zealand Honey
• • Text: “All specified values are averages.”
• • Not suitable for infants under 12 months. Do not use if cap seal is broken. Production methods involved with this product are not-GM. Contains bee products.
• • PET Recycling pictogram
• • Round corners
• Apart from different bird image each of 4 honey labels should have it's own color element e.g a different color background or a line.
• The birds:
• • Manuka honey: image of a Kingfisher bird
• o MGO Pictogram (80+, 100+, 200+, 300+ or 400+)
• • Rewarewa honey: image of a Kereru bird
• • Multifloral honey: image of a Tui bird
• • Manuka blend: image of a Pukekohe bird
Should not have
• Disclaimer: The provided images of birds is a copyright content. It is prohibited to use them outside of this project.

```html
<!DOCTYPE html>
<html lang="en">
<head>
<meta charset="utf-8">
<title>Velnor Honey Labels</title>
<link rel="stylesheet" href="https://fonts.googleapis.com/css2?family=Montserrat:wght@700;800&family=Oswald:wght@300;400&display=swap">
<style>
  :root{
    --canvas:#d3ab6b;
    --label-black:#05070b;
    --label-edge:#3a4048;
    --gold:#e8c565;
    --gold-soft:#d9b75a;
    --white:#ffffff;
    --band-manuka:#3a1859;
    --band-multifloral:#7a2f1f;
    --band-blend:#2b3d22;
    --band-rewarewa:#0f4770;
  }
  *{box-sizing:border-box;margin:0;padding:0}
  html,body{width:1200px;height:1200px;overflow:hidden;background:var(--canvas)}
  .sheet{position:relative;width:1200px;height:1200px}
  .label{
    position:absolute;width:440px;height:332px;border-radius:16px;overflow:hidden;
    background:linear-gradient(90deg,var(--label-edge) 0%,var(--label-black) 8%,var(--label-black) 92%,var(--label-edge) 100%);
  }
  .label--manuka{left:120px;top:200px;--band:var(--band-manuka)}
  .label--multifloral{left:640px;top:200px;--band:var(--band-multifloral)}
  .label--blend{left:120px;top:668px;--band:var(--band-blend)}
  .label--rewarewa{left:640px;top:668px;--band:var(--band-rewarewa)}
  .label__band{
    position:absolute;left:0;right:0;top:246px;bottom:0;z-index:0;
    background:linear-gradient(90deg,rgba(255,255,255,.18) 0%,var(--band) 8%,var(--band) 92%,rgba(255,255,255,.18) 100%);
  }
  .brand,.grade-badge,.product-name,.net-weight,.origin{z-index:2}
  .brand{
    position:absolute;left:0;right:0;top:34px;display:flex;align-items:center;justify-content:center;gap:10px;
    font-family:"Montserrat",sans-serif;font-weight:700;font-size:30px;letter-spacing:.14em;color:var(--gold);
  }
  .brand__dot{width:12px;height:12px;border-radius:50%;background:var(--gold)}
  .grade-badge{position:absolute;left:62px;top:122px;width:62px;height:32px}
  .product-name{
    position:absolute;left:62px;top:168px;white-space:nowrap;
    font-family:"Montserrat",sans-serif;font-weight:800;font-size:28px;line-height:32px;color:var(--white);
    text-transform:uppercase;letter-spacing:.01em;
  }
  .net-weight{
    position:absolute;left:62px;top:256px;
    font-family:"Oswald",sans-serif;font-weight:300;font-size:22px;color:var(--gold-soft);
  }
  .origin{
    position:absolute;left:62px;top:290px;
    font-family:"Oswald",sans-serif;font-weight:300;font-size:15px;color:var(--gold-soft);
  }
  .bird-art{position:absolute;z-index:1;left:290px;width:138px}
  .bird-art--kingfisher{top:136px;height:170px;background:radial-gradient(ellipse at 50% 45%,#35a9e0 0%,#1c5fb3 40%,rgba(232,120,40,.3) 62%,transparent 72%)}
  .bird-art--tui{top:134px;height:170px;background:radial-gradient(ellipse at 50% 45%,#1f7a86 0%,#16395a 40%,rgba(240,170,30,.3) 62%,transparent 72%)}
  .bird-art--pukeko{top:112px;height:212px;background:radial-gradient(ellipse at 50% 45%,#4b5bc0 0%,#2b2a78 40%,rgba(60,160,60,.3) 62%,transparent 72%)}
  .bird-art--kereru{top:118px;height:206px;background:radial-gradient(ellipse at 50% 45%,#a44aa8 0%,#3a5fa8 40%,rgba(40,140,90,.3) 62%,transparent 72%)}
</style>
</head>
<body>
<main class="sheet">

  <section class="label label--manuka">
    <div class="label__band"></div>
    <div class="bird-art bird-art--kingfisher" role="img" aria-label="Faceted illustration of a kingfisher perched on a branch"></div>
    <div class="brand"><span class="brand__dot"></span>VELNOR</div>
    <svg class="grade-badge" viewBox="0 0 62 32" aria-hidden="true"><polygon points="8,2 54,2 60,16 54,30 8,30 2,16" fill="none" stroke="var(--gold)" stroke-width="2"/></svg>
    <h2 class="product-name">Manuka<br>Honey</h2>
    <p class="net-weight">Net. 1 Kg</p>
    <p class="origin">Product of New Zealand</p>
  </section>

  <section class="label label--multifloral">
    <div class="label__band"></div>
    <div class="bird-art bird-art--tui" role="img" aria-label="Faceted illustration of a tui on a branch with orange flowers"></div>
    <div class="brand"><span class="brand__dot"></span>VELNOR</div>
    <h2 class="product-name">Multifloral<br>Honey</h2>
    <p class="net-weight">Net. 1 Kg</p>
    <p class="origin">Product of New Zealand</p>
  </section>

  <section class="label label--blend">
    <div class="label__band"></div>
    <div class="bird-art bird-art--pukeko" role="img" aria-label="Faceted illustration of a pukeko standing in grass"></div>
    <div class="brand"><span class="brand__dot"></span>VELNOR</div>
    <svg class="grade-badge" viewBox="0 0 62 32" aria-hidden="true"><polygon points="8,2 54,2 60,16 54,30 8,30 2,16" fill="none" stroke="var(--gold)" stroke-width="2"/></svg>
    <h2 class="product-name">Manuka<br>Blend Honey</h2>
    <p class="net-weight">Net. 1 Kg</p>
    <p class="origin">Product of New Zealand</p>
  </section>

  <section class="label label--rewarewa">
    <div class="label__band"></div>
    <div class="bird-art bird-art--kereru" role="img" aria-label="Faceted illustration of a kereru on a leafy branch"></div>
    <div class="brand"><span class="brand__dot"></span>VELNOR</div>
    <h2 class="product-name">Rewarewa<br>Honey</h2>
    <p class="net-weight">Net. 1 Kg</p>
    <p class="origin">Product of New Zealand</p>
  </section>

</main>
</body>
</html>
```